Website re-design

We are a successful furnished apartment provider in Boston. We currently are working on re-designing our website www.ribtenlofts.com to make it more modern, designer look and user friendly. We hired a designer, but are not happy with the designs proposed and want to improve on them. The winning design will be paid regardless of whether we stay with our current designer or not. We want ideas and functional page links to see how it will work. Platform we have chosen is wordpress. Feel free to propose others easy for us to update and modify. We do not like Joomla on which website is currently running. We do not like flash nor long load times.
Please use photos on our website for design presentations. www.ribtenlofts.com

Target Market(s)

doctors, nurses, business men but mostly business women, some post-medical students

Industry/Entity Type

Apartment

Requirements
Must have
• Quick action button for reservation form and a notification and email forwarding system to us of reservation information by potential clients. Blog required with feedback by guests allowed, we can censor which are published. Slide shows of apartments.
Should not have
• No movies.

```html
<!DOCTYPE html>
<html lang="en">
<head>
<meta charset="utf-8">
<title>Ribten Lofts Furnished Apartments</title>
<link rel="stylesheet" href="https://fonts.googleapis.com/css2?family=PT+Sans:wght@400;700&family=Droid+Sans&family=Arimo:wght@400&display=swap">
<style>
  :root {
    --ink-black: #000000;
    --gold: #c9ab6a;
    --nav-blue: #1b3d66;
    --heading-blue: #1d4d72;
    --body-grey: #4f4f4f;
    --page-grey: #f3f3f3;
    --band-top: #2b3446;
    --band-bottom: #5b7e92;
    --muted: #8a8a8a;
    --rss: #f08a1c;
  }
  * { margin: 0; padding: 0; box-sizing: border-box; }
  html, body { width: 1200px; height: 885px; overflow: hidden; }
  body {
    position: relative;
    background: var(--page-grey);
    font-family: "PT Sans", sans-serif;
  }
  .site-header {
    position: absolute; left: 0; top: 0; width: 1200px; height: 97px;
    background: var(--ink-black);
  }
  .brand {
    position: absolute; left: 137px; top: 18px; height: 68px;
    display: flex; align-items: center; gap: 12px;
  }
  .brand-dot {
    width: 60px; height: 60px; border-radius: 50%; background: var(--gold);
  }
  .brand-name {
    font-family: "PT Sans", sans-serif; font-size: 27px; font-weight: 400;
    color: var(--gold); letter-spacing: 1px; text-transform: uppercase;
  }
  .search {
    position: absolute; left: 843px; top: 24px; width: 176px; height: 29px;
    border-radius: 5px; background: linear-gradient(#e9e9e9, #ffffff);
    border: 1px solid #bbb; font-family: "Arimo", sans-serif; font-size: 13px;
    color: #aaa; padding: 6px 14px;
  }
  .search-button {
    position: absolute; left: 1025px; top: 24px; width: 36px; height: 29px;
    border-radius: 5px; background: linear-gradient(#ffffff, #dcdcdc);
    border: 1px solid #bbb;
  }
  .search-button svg { position: absolute; left: 9px; top: 6px; }
  .phone {
    position: absolute; right: 140px; top: 64px;
    font-family: "Arimo", sans-serif; font-size: 16px; color: #c8c8c8;
    white-space: nowrap;
  }
  .header-rule {
    position: absolute; left: 0; top: 97px; width: 1200px; height: 20px;
    background: linear-gradient(#f0f0f0 0, #d8d8d8 40%, #8f8f8f 75%, #222 100%);
  }
  .main-nav {
    position: absolute; left: 0; top: 117px; width: 1200px; height: 38px;
    background: linear-gradient(#ffffff, #e4e4e4);
    border-bottom: 1px solid #b8b8b8;
  }
  .nav-link {
    position: absolute; top: 12px; font-family: "Arimo", sans-serif;
    font-size: 12px; color: var(--nav-blue); text-transform: uppercase;
    text-decoration: none;
  }
  .nav-link.current {
    top: 5px; left: 176px; width: 78px; height: 27px; padding-top: 7px;
    text-align: center; color: #444; border-radius: 4px;
    background: linear-gradient(#fafafa, #cfcfcf); border: 1px solid #a8a8a8;
  }
  .log-in { position: absolute; left: 979px; top: 12px; font-family: "Arimo", sans-serif; font-size: 12px; color: var(--muted); }
  .rss { position: absolute; left: 1035px; top: 12px; }
  .hero-band {
    position: absolute; left: 0; top: 155px; width: 1200px; height: 321px;
    background: linear-gradient(var(--band-top), var(--band-bottom));
  }
  .hero-fade {
    position: absolute; left: 0; top: 476px; width: 1200px; height: 60px;
    background: linear-gradient(#d6d6d6, var(--page-grey));
  }
  .hero-shadow {
    position: absolute; left: 165px; top: 596px; width: 870px; height: 38px;
    border-radius: 50% / 0 0 100% 100%;
    background: radial-gradient(ellipse at 50% 0, rgba(0,0,0,0.75), rgba(0,0,0,0) 70%);
  }
  .hero-slide {
    position: absolute; left: 138px; top: 165px; width: 924px; height: 431px;
    background:
      linear-gradient(180deg, rgba(235,228,214,0.9) 0%, rgba(150,130,110,0.6) 55%, rgba(120,70,30,0.9) 100%),
      linear-gradient(90deg, #d9d4ca, #8a7a66 60%, #3a3a3e);
  }
  .welcome {
    position: absolute; left: 139px; top: 668px;
    font-size: 29px; font-weight: 400; color: var(--heading-blue);
    white-space: nowrap;
  }
  .welcome-rule {
    position: absolute; left: 190px; top: 733px; width: 760px; height: 4px;
    background: linear-gradient(90deg, rgba(0,0,0,0), rgba(0,0,0,0.18) 50%, rgba(0,0,0,0));
  }
  .intro {
    position: absolute; left: 145px; top: 772px; width: 900px;
    font-family: "Droid Sans", "PT Sans", sans-serif; font-size: 24px;
    line-height: 35.5px; color: var(--body-grey);
  }
</style>
</head>
<body>
  <header class="site-header">
    <div class="brand">
      <span class="brand-dot"></span>
      <span class="brand-name">Ribten Lofts</span>
    </div>
    <div class="search">Search...</div>
    <div class="search-button">
      <svg width="18" height="18" viewBox="0 0 18 18"><circle cx="7" cy="7" r="5" fill="none" stroke="#666" stroke-width="2"/><line x1="11" y1="11" x2="16" y2="16" stroke="#666" stroke-width="3" stroke-linecap="round"/></svg>
    </div>
    <div class="phone">Call Us Free: 1-800- 555-0182</div>
  </header>
  <div class="header-rule"></div>
  <nav class="main-nav">
    <a class="nav-link current" href="#">Home</a>
    <a class="nav-link" style="left:273px" href="#">Apartments</a>
    <a class="nav-link" style="left:377px" href="#">Reservation</a>
    <a class="nav-link" style="left:488px" href="#">Reviews</a>
    <a class="nav-link" style="left:575px" href="#">Blog</a>
    <a class="nav-link" style="left:642px" href="#">Contact</a>
    <a class="nav-link" style="left:732px" href="#">Boston</a>
    <a class="nav-link" style="left:815px" href="#">About Us</a>
    <span class="log-in">Log In</span>
    <svg class="rss" width="16" height="16" viewBox="0 0 16 16"><rect width="16" height="16" rx="3" fill="var(--rss)"/><circle cx="4.5" cy="11.5" r="1.6" fill="#fff"/><path d="M3 7a6 6 0 0 1 6 6" fill="none" stroke="#fff" stroke-width="1.8"/><path d="M3 3.5a9.5 9.5 0 0 1 9.5 9.5" fill="none" stroke="#fff" stroke-width="1.8"/></svg>
  </nav>
  <div class="hero-band"></div>
  <div class="hero-fade"></div>
  <div class="hero-shadow"></div>
  <div class="hero-slide" role="img" aria-label="Slideshow photo of a furnished apartment living room with tall curtained windows, armchairs, a coffee table on a rug, a mirrored wardrobe, a fireplace and a bed"></div>
  <h1 class="welcome">Welcome to Ribten Lofts Furnished Apartments</h1>
  <div class="welcome-rule"></div>
  <p class="intro">Ribten Lofts is proud to offer some of the best furnished apartments in Boston.<br>Our locations are in the trendiest area of the city: the South End.<br>In the South End neighborhood, you will find wonderful restaurants,</p>
</body>
</html>
```